Outdoor mass notification company needing business card design.

Our company name is Harrowgate Signal Systems Inc located in Amory Mississippi and we sell and maintain "Brantor" Mass Notification Sirens in the US. Outdoor sirens notify people of certain severe dangers such as tornados, severe thunderstorms, flooding, hurricanes and tsunamis. We also serve the oil and gas refining industries to warn of Chemical releases, fires, and lightning alerts.

Contact Information for Business Card

Name, title, cell number, email address

Requirements
Nice to have
• The Brantor logo and also the Mildvane logo.

```html
<!DOCTYPE html>
<html lang="en">
<head>
<meta charset="utf-8">
<title>Harrowgate Signal Systems – Business Card</title>
<link rel="stylesheet" href="https://fonts.googleapis.com/css2?family=EB+Garamond:wght@700&family=Roboto+Slab:wght@300;400;700&display=swap">
<style>
  :root {
    --backdrop: #d4d5d7;
    --card-dark: #181717;
    --card-light: #ffffff;
    --brand-muted: #3f5b7b;
    --brand-navy: #25405e;
    --text-grey: #4a4a4a;
    --icon-navy: #25405e;
  }
  * { margin: 0; padding: 0; box-sizing: border-box; }
  html, body { width: 900px; height: 1200px; overflow: hidden; }
  body { background: var(--backdrop); position: relative; font-family: "Roboto Slab", serif; }

  .card { position: absolute; width: 633px; height: 364px; overflow: hidden; }
  .card-front { left: 133px; top: 210px; background: var(--card-dark); }
  .card-back { left: 134px; top: 624px; background: var(--card-light); }

  .wordmark { font-family: "EB Garamond", serif; font-weight: 700; text-transform: uppercase; line-height: 1; }
  .card-front .wordmark {
    position: absolute; left: 0; right: 0; top: 150px; text-align: center;
    color: var(--brand-muted);
  }
  .card-front .wordmark .line-1 { display: block; font-size: 48px; letter-spacing: 0.5px; }
  .card-front .wordmark .line-2 { display: block; font-size: 36px; margin-top: 4px; }

  .card-back .wordmark { position: absolute; left: 32px; top: 42px; color: var(--brand-navy); }
  .card-back .wordmark .line-1 { display: block; font-size: 30px; padding-left: 40px; }
  .card-back .wordmark .line-2 { display: block; font-size: 23px; margin-top: 3px; }

  .holder { position: absolute; left: 30px; top: 186px; }
  .holder-name { font-weight: 700; font-size: 23px; color: var(--brand-navy); letter-spacing: 0.3px; }
  .holder-title { font-weight: 400; font-size: 16px; color: var(--text-grey); margin-top: 2px; }

  .contact-list { position: absolute; left: 30px; top: 248px; list-style: none; }
  .contact-list li {
    display: flex; align-items: center; height: 23px;
    font-weight: 300; font-size: 14px; color: #333; letter-spacing: 0.6px;
  }
  .contact-list li.phone { letter-spacing: 2px; }
  .contact-list li.address { letter-spacing: 0; }
  .contact-list svg { width: 14px; height: 14px; margin-right: 8px; fill: var(--icon-navy); flex: none; }

  .product-photo { position: absolute; }
  .horn-array {
    left: 380px; top: 49px; width: 228px; height: 205px;
    background: linear-gradient(135deg, #e4e2e1 0%, #bdbab8 55%, #8e8b89 100%);
  }
  .siren-row {
    left: 368px; top: 238px; width: 254px; height: 126px;
    background: linear-gradient(180deg, #3a3a3a 0%, #1e1e1e 100%);
    clip-path: polygon(0 0, 100% 68%, 100% 100%, 0 100%);
  }
</style>
</head>
<body>

<section class="card card-front">
  <div class="wordmark">
    <span class="line-1">Harrowgate</span>
    <span class="line-2">Signal Systems</span>
  </div>
</section>

<section class="card card-back">
  <div class="wordmark">
    <span class="line-1">Harrowgate</span>
    <span class="line-2">Signal Systems</span>
  </div>

  <div class="holder">
    <div class="holder-name">DALEN ASHCROFT</div>
    <div class="holder-title">Owner</div>
  </div>

  <ul class="contact-list">
    <li class="phone">
      <svg viewBox="0 0 24 24"><path d="M6.6 10.8a15.1 15.1 0 0 0 6.6 6.6l2.2-2.2c.3-.3.7-.4 1-.2 1.1.4 2.3.6 3.6.6.6 0 1 .4 1 1V20c0 .6-.4 1-1 1A17 17 0 0 1 3 4c0-.6.4-1 1-1h3.5c.6 0 1 .4 1 1 0 1.3.2 2.5.6 3.6.1.3 0 .7-.2 1l-2.3 2.2z"/></svg>
      (555) 014-2270
    </li>
    <li class="email">
      <svg viewBox="0 0 24 24"><path d="M2 5h20v14H2z M3 6l9 7 9-7" fill="none"/><path d="M2 5h20v14H2V5zm2 2v.4l8 6 8-6V7l-8 6-8-6z"/></svg>
      info@harrowgatesignal.com
    </li>
    <li class="web">
      <svg viewBox="0 0 24 24"><circle cx="12" cy="12" r="10" fill="none" stroke="#25405e" stroke-width="2"/><path d="M2 12h20M12 2v20" stroke="#25405e" stroke-width="1.6"/><ellipse cx="12" cy="12" rx="4.5" ry="10" fill="none" stroke="#25405e" stroke-width="1.6"/><path d="M4 7h16M4 17h16" stroke="#25405e" stroke-width="1.4"/></svg>
      www.harrowgatesignal.com
    </li>
    <li class="address">
      <svg viewBox="0 0 24 24"><path d="M12 2a7 7 0 0 0-7 7c0 5 7 13 7 13s7-8 7-13a7 7 0 0 0-7-7zm0 9.5A2.5 2.5 0 1 1 12 6.5a2.5 2.5 0 0 1 0 5z"/></svg>
      4120 County Rd 18 Amory, MS 38821
    </li>
  </ul>

  <div class="product-photo horn-array" role="img" aria-label="Photo of a grey outdoor warning siren with four horns on a rotating base"></div>
  <div class="product-photo siren-row" role="img" aria-label="Photo of a row of black stacked omnidirectional sirens decreasing in size"></div>
</section>

</body>
</html>
```